Premium modern eliquids labels 84.5 x 80 mm

I am looking for modern graphics for the labels of a new eliquid line that will have 4 different types of eliquids. It will have a tobacco one (brown colours maybe), a fruity one (bright colours maybe), a minty one (green colours maybe) and a creamy one (beige colours maybe).
I will need one of them to see how the design is, that design will have to be adapted to the other 3 colours of the label.
The brand logo is attached. I also attached a sample of what is mandatory to write on the label, you can change size, place and font of what is written, the only thing that cannot be reduced is the yellow parts. I attach the bottle that we will use.The size of the label is 84.5 x 80 mm (base x height).

Target Market(s)

vapers

Requirements
Must have
• My project must have one of the labels.

```html
<!DOCTYPE html>
<html lang="it">
<head>
<meta charset="utf-8">
<title>Velvet Drop – Creamy label</title>
<link href="https://fonts.googleapis.com/css2?family=Open+Sans:wght@400;700;800&family=Great+Vibes&display=swap" rel="stylesheet">
<style>
:root{
  --page:#ffffff;
  --cream-light:#faf1ea;
  --cream-mid:#f5e3d4;
  --cream-edge:#efcfb0;
  --brown:#5a2c0f;
  --band:#663409;
  --text:#4a2a14;
  --brand:#7dbde6;
  --yellow:#fcc72b;
  --swirl-a:#fffaf5;
  --swirl-b:#ecc7a6;
}
*{margin:0;padding:0;box-sizing:border-box}
html,body{width:1200px;height:2367px;overflow:hidden;background:var(--page)}
body{position:relative;font-family:"Open Sans",Arial,sans-serif;color:var(--text)}
.label-surface{
  background:radial-gradient(ellipse at 35% 45%,var(--cream-light) 0%,var(--cream-mid) 60%,var(--cream-edge) 100%);
}
.front-label{position:absolute;left:469px;top:590px;width:248px;height:653px}
.flat-label{position:absolute;left:161px;top:1402px;width:866px;height:807px;overflow:hidden}
.abs{position:absolute}
.brand{
  position:absolute;left:0;right:0;text-align:center;
  font-weight:800;color:var(--brand);letter-spacing:1px;line-height:1;
}
.brand-dot{display:inline-block;width:.45em;height:.45em;border-radius:50%;background:var(--brand);margin-right:.3em;vertical-align:middle}
.swirl{
  position:absolute;border-radius:50%;
  background:radial-gradient(circle at 50% 50%,var(--swirl-b) 0%,var(--swirl-a) 45%,rgba(255,250,245,0) 72%);
}
.flavour-name{
  position:absolute;left:0;right:0;text-align:center;
  font-family:"Great Vibes",cursive;color:var(--brown);line-height:1;
}
.flavour-sub{
  position:absolute;left:0;right:0;text-align:center;
  font-size:13px;letter-spacing:6px;color:var(--text);
}
.net{position:absolute;left:0;right:0;text-align:center;font-weight:700;color:var(--brown)}
.side-band{position:absolute;left:0;top:0;width:47px;height:100%;background:var(--band)}
.lot-code{
  position:absolute;left:23px;top:50%;
  transform:translate(-50%,-50%) rotate(-90deg);
  white-space:nowrap;color:#fff;font-weight:700;font-size:21px;
}
.info{font-size:20px;line-height:29px;color:var(--text)}
.info strong{font-weight:700;color:var(--brown)}
.ingredients{left:68px;top:106px;width:200px}
.instructions{left:620px;top:121px;width:220px}
.producer{left:68px;top:522px;width:260px}
.tag-yellow{position:absolute;background:var(--yellow);color:var(--brown);font-weight:700}
.tag-small{font-size:13px;line-height:15px;padding:4px 12px}
.tag-big{font-size:20px;padding:3px 8px;line-height:30px}
.tag-caption{position:absolute;font-size:16px;color:var(--text)}
.icons{position:absolute;left:620px;top:660px}
</style>
</head>
<body>

<section class="front-label label-surface">
  <div class="brand" style="top:112px;font-size:26px"><span class="brand-dot"></span>VELVET DROP</div>
  <div class="swirl" role="img" aria-label="Soft cream swirl" style="left:36px;top:247px;width:176px;height:176px"></div>
  <div class="flavour-name" style="top:460px;font-size:80px">Creamy</div>
  <div class="flavour-sub" style="top:532px;font-size:12px">FLAVORED</div>
  <div class="net" style="top:616px;font-size:18px">20 ML NET</div>
</section>

<section class="flat-label label-surface">
  <div class="side-band"><div class="lot-code">L.SH20 - 001-PES-D.PROD.22-04-2022 D.SC.21-04-2024</div></div>

  <div class="abs info ingredients"><strong>INGREDIENTI:</strong><br>Glicolepropilenico sostanzearomatiz zanti</div>

  <div class="brand" style="top:125px;left:294px;right:auto;width:280px;font-size:34px"><span class="brand-dot"></span>VELVET DROP</div>

  <div class="abs info instructions"><strong>ISTRUZIONI D'USO:</strong><br>Agitare bene prima dell'utilizzo. Diluire nelle percentuali consigliate sul nostro sito. Conservare in luogo fresco e asciutto</div>

  <div class="swirl" role="img" aria-label="Soft cream swirl" style="left:317px;top:272px;width:234px;height:234px"></div>

  <div class="flavour-name" style="top:525px;left:294px;right:auto;width:280px;font-size:94px">Creamy</div>
  <div class="flavour-sub" style="top:620px;left:294px;right:auto;width:280px">FLAVORED</div>
  <div class="net" style="top:716px;left:294px;right:auto;width:280px;font-size:21px">20 ML NET</div>

  <div class="abs info producer"><strong>PRODOTTO<br>E CONFEZIONATO<br>DA</strong> Nordale srl<br>Via Lago 18<br>10100 Torino<br>P.i.00000000000<br>Tel. +39 000 0000000<br>info@nordale.it</div>

  <div class="tag-yellow tag-small" style="left:620px;top:393px;width:122px">RACCOLTA<br>PLASTICA</div>
  <div class="tag-caption" style="left:623px;top:432px;font-weight:700;color:var(--brown)">ETICHETTA</div>
  <div class="tag-yellow tag-big" style="left:620px;top:456px">PAP 5</div>

  <div class="tag-yellow tag-small" style="left:620px;top:518px;width:122px">RACCOLTA<br>PLASTICA</div>
  <div class="tag-caption" style="left:628px;top:554px">FLACONE</div>
  <div class="tag-yellow tag-big" style="left:620px;top:578px">PET 1</div>

  <svg class="icons" width="140" height="80" viewBox="0 0 140 80" aria-label="Recycling and disposal icons" role="img">
    <g fill="none" stroke="var(--text)" stroke-width="2.5" stroke-linejoin="round">
      <path d="M30 12 L18 34 M22 32 L18 34 L16 29"/>
      <path d="M36 14 L48 34 M44 33 L48 34 L50 29"/>
      <path d="M44 46 L18 46 M22 42 L18 46 L22 50"/>
      <path d="M14 40 L10 46 L24 60 M40 60 L54 46 L50 40"/>
    </g>
    <g fill="var(--text)">
      <path d="M80 30 h30 l-4 42 h-22 z"/>
      <rect x="77" y="24" width="36" height="5"/>
    </g>
  </svg>
</section>

</body>
</html>
```